PowerPoint template for my training workshop business

I would like to have a PowerPoint template created using my logo and palette materials created by Brindlework. I train and facilitate workshops using PowerPoint in both corporate and public settings.

I have attached the original design elements to this request.

```html
<!DOCTYPE html>
<html lang="en">
<head>
<meta charset="utf-8">
<title>Marisol Keene Coaching – Presentation Template</title>
<link href="https://fonts.googleapis.com/css2?family=Poppins:wght@400;500;600;700&display=swap" rel="stylesheet">
<style>
:root{
  --stage:#6f6f6f;
  --orange:#f7941d;
  --charcoal:#242424;
  --header:#4b4b4b;
  --header-hi:#5a5a5a;
  --ink:#222;
  --line:#e3e3e3;
  --white:#fff;
}
*{margin:0;padding:0;box-sizing:border-box}
html,body{width:1200px;height:995px;overflow:hidden;background:var(--stage)}
body{position:relative;font-family:"Poppins",sans-serif;color:var(--ink)}
.slide{position:absolute;width:558px;height:313px;background:var(--white);overflow:hidden}
.s-title{left:11px;top:8px;background:radial-gradient(circle at 75% 40%,#3a3a3a,var(--charcoal) 70%)}
.s-courses{left:589px;top:8px}
.s-clients{left:11px;top:336px}
.s-info{left:584px;top:336px}
.s-services{left:11px;top:662px}
.s-reports{left:582px;top:662px}
.abs{position:absolute}
.header{position:absolute;left:0;top:0;width:100%;height:42px;background:linear-gradient(90deg,var(--header),var(--header-hi));display:flex;align-items:center;justify-content:space-between;padding:0 12px 0 14px}
.header h2{color:var(--white);font-weight:700;font-size:19px;letter-spacing:.2px}
.brand{display:flex;align-items:center;gap:6px}
.brand-dot{width:24px;height:24px;border-radius:50%;background:var(--orange);flex:none}
.brand-name{font-family:"Poppins",sans-serif;font-weight:600;color:var(--orange);font-size:9px;white-space:nowrap}
.footer{position:absolute;left:0;bottom:0;width:100%;height:13px;background:var(--orange);font-size:6px;color:#fff6e8;padding:3px 3px 0}
.page-no{position:absolute;right:10px;bottom:3px;width:26px;height:26px;border-radius:50%;background:#2e2e2e;border:2px solid var(--white);color:var(--white);font-size:7px;font-weight:600;display:flex;align-items:center;justify-content:center}
.lorem{font-size:5.5px;line-height:1.7;color:#555}
.photo{position:absolute}
/* title slide */
.title-main{right:26px;top:86px;text-align:right;color:var(--white);font-weight:700;font-size:35px;line-height:1.08}
.title-sub{left:322px;top:162px;width:211px;border-top:1px solid #8a8a8a;border-bottom:1px solid #8a8a8a;color:var(--white);font-size:13px;font-weight:500;text-align:right;height:32px;line-height:30px}
.coach-name{left:70px;top:255px;width:130px;text-align:center;color:var(--orange);font-weight:500;font-size:12px}
.coach-role{left:70px;top:271px;width:130px;text-align:center;color:var(--white);font-size:9px;font-weight:500}
.title-brand{left:300px;top:238px;gap:10px}
.title-brand .brand-dot{width:40px;height:40px}
.title-brand .brand-name{font-size:15px}
/* courses */
.courses-head{left:307px;top:74px;color:var(--orange);font-weight:700;font-size:14px}
.courses-intro{left:307px;top:94px;width:200px}
.course-item{left:318px;width:200px;display:flex;gap:8px}
.course-icon{width:22px;height:22px;border-radius:50%;border:1.5px solid var(--orange);flex:none;display:flex;align-items:center;justify-content:center;background:#fff7ee}
.course-item h4{color:var(--orange);font-size:8px;font-weight:500;line-height:1.2}
.courses-label{left:62px;top:158px;width:160px;text-align:center;color:var(--orange);font-weight:600;font-size:14px}
/* clients */
.clients-intro{left:35px;top:74px;width:280px;font-size:7px;line-height:1.75}
.point{left:34px;width:200px;display:flex;gap:8px}
.num{width:24px;height:24px;border-radius:50%;background:var(--orange);color:#fff;font-size:8px;font-weight:600;display:flex;align-items:center;justify-content:center;flex:none}
.point h4{font-size:9.5px;font-weight:500;line-height:1.3}
.client{position:absolute;width:70px;height:70px;border-radius:50%;background:var(--white);border:1px solid var(--line);box-shadow:0 0 4px rgba(0,0,0,.06);display:flex;align-items:center;justify-content:center;text-align:center;font-size:9px;font-weight:600;color:#2d3f7a;line-height:1.1;padding:6px}
/* infographics */
.ribbon{position:absolute;color:#fff;font-size:5.5px;line-height:1.7;padding:10px 30px 0 22px}
.ribbon b{display:block;font-size:7px;font-weight:600}
/* services */
.card{position:absolute;width:124px;height:96px;border:1px solid #e4e4e4;border-radius:14px;background:var(--white);text-align:center;padding-top:12px}
.card .tag{display:inline-block;width:22px;height:20px;border-radius:4px;background:var(--orange);color:#fff;font-size:8px;font-weight:600;line-height:20px}
.card h4{font-size:7px;font-weight:500;margin:10px 0 3px}
.card p{font-size:5px;line-height:1.75;color:#666;padding:0 8px}
/* reports */
.stat{position:absolute;left:383px}
.stat h4{font-size:7px;font-weight:600}
.stat .lorem{width:100px}
</style>
</head>
<body>

<!-- Title slide -->
<section class="slide s-title">
  <svg class="abs" style="left:44px;top:66px" width="182" height="182" viewBox="0 0 182 182">
    <path d="M91 4 A87 87 0 0 1 150 155" fill="none" stroke="#f7941d" stroke-width="9" stroke-linecap="round"/>
    <path d="M22 40 A87 87 0 0 0 60 170" fill="none" stroke="#a9adb8" stroke-width="7" stroke-linecap="round"/>
  </svg>
  <div class="photo" role="img" aria-label="Portrait photo of the coach" style="left:63px;top:85px;width:144px;height:144px;border-radius:50%;background:radial-gradient(circle at 50% 40%,#c29a7c,#6d4d3a 75%)"></div>
  <p class="abs coach-name">MARISOL KEENE</p>
  <p class="abs coach-role">LIFE COACH</p>
  <h1 class="abs title-main">PERSENTATION<br>TITLE HERE</h1>
  <p class="abs title-sub">SUBTEXT HERE SUBTEXT HERE</p>
  <div class="abs brand title-brand"><span class="brand-dot"></span><span class="brand-name">Marisol Keene Coaching</span></div>
</section>

<!-- Training courses -->
<section class="slide s-courses">
  <header class="header"><h2>OUR TRAINING COURSES</h2><div class="brand"><span class="brand-dot"></span><span class="brand-name">Marisol Keene Coaching</span></div></header>
  <svg class="abs" style="left:37px;top:61px" width="210" height="210" viewBox="0 0 210 210">
    <path d="M121.7 10.5 A96 96 0 1 1 57 188.1" fill="none" stroke="#f7941d" stroke-width="7" stroke-linecap="round"/>
    <path d="M47.1 36.1 A94 94 0 0 0 27.1 150" fill="none" stroke="#9ea3ad" stroke-width="3"/>
  </svg>
  <div class="photo" role="img" aria-label="Photo of a laptop workspace under dark overlay" style="left:52px;top:76px;width:180px;height:180px;border-radius:50%;background:radial-gradient(circle at 60% 45%,#5a5d60,#2f3235 80%)"></div>
  <p class="abs courses-label">OUR COURSES</p>
  <h3 class="abs courses-head">OUR TRAINING COURSES</h3>
  <p class="abs lorem courses-intro">Lorem ipsum dolor sit amet, consectetur adipi scing elit, sed do eiusmod tempor incididunt ut labore et dolore magna aliqua.</p>
  <div class="abs course-item" style="top:120px"><span class="course-icon"><svg width="10" height="10"><rect x="1" y="2" width="8" height="6" fill="none" stroke="#f7941d"/></svg></span><div><h4>Icons Heading Here</h4><p class="lorem">Lorem ipsum dolor sit amet, consectetur adipisicing elit, sed do eiusmod tempor incididunt ut labor aliqua.</p></div></div>
  <div class="abs course-item" style="top:160px"><span class="course-icon"><svg width="10" height="10"><circle cx="5" cy="4" r="3" fill="none" stroke="#f7941d"/><path d="M4 8h2" stroke="#f7941d"/></svg></span><div><h4>Icons Heading Here</h4><p class="lorem">Lorem ipsum dolor sit amet, consectetur adipisicing elit, sed do eiusmod tempor incididunt ut labor aliqua.</p></div></div>
  <div class="abs course-item" style="top:200px"><span class="course-icon"><svg width="10" height="10"><rect x="2" y="1" width="6" height="8" fill="none" stroke="#f7941d"/></svg></span><div><h4>Icons Heading Here</h4><p class="lorem">Dolor sit amet, consectetur adipisicing elit, sed do eiusmod tempor incididunt ut labor aliqua.</p></div></div>
  <div class="abs course-item" style="top:242px"><span class="course-icon"><svg width="10" height="10"><rect x="2" y="1" width="6" height="8" fill="none" stroke="#f7941d"/></svg></span><div><h4>Icons Heading Here</h4><p class="lorem">Dolor sit amet, consectetur adipisicing elit, sed do eiusmod tempor incididunt ut labor aliqua.</p></div></div>
  <footer class="footer">Copyright text here</footer>
  <span class="page-no">01</span>
</section>

<!-- Clients -->
<section class="slide s-clients">
  <header class="header"><h2>OUR CLIENTS</h2><div class="brand"><span class="brand-dot"></span><span class="brand-name">Marisol Keene Coaching</span></div></header>
  <p class="abs lorem clients-intro">Lorem ipsum dolor sit amet, consectetur adipi scing elit, sed do eiusmod tempor incididunt ut labore et dolore magna aliqua.</p>
  <div class="abs point" style="top:115px"><span class="num">01</span><div><h4>Experience</h4><p class="lorem">Lorem ipsum dolor sit amet, consectetur adipisicing elit, sed do eiusmod tempor incididunt ut labor aliqua.</p></div></div>
  <div class="abs point" style="top:162px"><span class="num">02</span><div><h4>Excellence</h4><p class="lorem">Ipsum dolor sit amet, consectetur adipisicing elit, sed do eiusmod tempor incididunt ut labor aliqua.</p></div></div>
  <div class="abs point" style="top:209px"><span class="num">03</span><div><h4>Effective</h4><p class="lorem">Dolor sit amet, consectetur adipisicing elit, sed do eiusmod tempor incididunt ut labor aliqua.</p></div></div>
  <div class="client" style="left:326px;top:77px">Ridgeway Fuel</div>
  <div class="client" style="left:396px;top:73px">Stonefield</div>
  <div class="client" style="left:288px;top:139px">Harlow</div>
  <div class="client" style="left:360px;top:139px">Northvale</div>
  <div class="client" style="left:431px;top:139px">Kestra</div>
  <div class="client" style="left:324px;top:205px">Orwin</div>
  <div class="client" style="left:399px;top:199px">Tidemark</div>
  <footer class="footer">Copyright text here</footer>
  <span class="page-no">01</span>
</section>

<!-- Infographics -->
<section class="slide s-info">
  <header class="header"><h2>OUR INFOGRAPHICS</h2><div class="brand"><span class="brand-dot"></span><span class="brand-name">Marisol Keene Coaching</span></div></header>
  <div class="photo" role="img" aria-label="Photo of hands writing in a spiral notebook" style="left:0;top:42px;width:300px;height:258px;background:linear-gradient(90deg,#a89a92 0%,#c9bcb4 45%,rgba(255,255,255,0) 100%)"></div>
  <svg class="abs" style="left:0;top:0" width="558" height="313">
    <path d="M219 130 H270 V70 H280 M254 180 H304 M219 230 H270 V242 H280" fill="none" stroke="#bbb" stroke-width=".8"/>
    <path d="M218 138 A42 42 0 0 0 218 222" fill="none" stroke="#f7941d" stroke-width="3"/>
    <circle cx="218" cy="180" r="40" fill="#e9e9e9"/>
    <circle cx="218" cy="180" r="33" fill="#fff"/>
    <g fill="none" stroke="#f7941d" stroke-width="1.2"><circle cx="218" cy="176" r="7"/><path d="M215 184h6M216 187h4M218 163v-3M207 168l-2-2M229 168l2-2"/></g>
    <polygon points="290,70 496,70 480,97 496,124 290,124 280,97" fill="#f7941d"/>
    <polygon points="314,142 525,142 508,169 525,196 314,196 304,169" fill="#4a4a4a"/>
    <polygon points="290,214 496,214 480,241 496,269 290,269 279,241" fill="#f7941d"/>
  </svg>
  <div class="ribbon" style="left:280px;top:78px;width:216px">Lorem ipsum dolor sit amet, consectetur adipisicing elit, sed do eiusmod tempor incididunt ut labor aliqua.</div>
  <div class="ribbon" style="left:304px;top:142px;width:221px"><b>Finding Creative Solutions</b>Lorem ipsum dolor sit amet, consectetur adipisicing elit, sed do eiusmod tempor incididunt ut labor aliqua.</div>
  <div class="ribbon" style="left:279px;top:214px;width:216px"><b>Solving Problem With Confident</b>Lorem ipsum dolor sit amet, consectetur adipisicing elit, sed do eiusmod tempor incididunt ut labor aliqua.</div>
  <footer class="footer">Copyright text here</footer>
  <span class="page-no">01</span>
</section>

<!-- Coach services -->
<section class="slide s-services">
  <header class="header"><h2>OUR COACH SERVICES</h2><div class="brand"><span class="brand-dot"></span><span class="brand-name">Marisol Keene Coaching</span></div></header>
  <div class="card" style="left:85px;top:74px"><span class="tag">01</span><h4>Services - 01</h4><p>Lorem ipsum dolor sit amet, consectetur adipisicing elit, sed do eiusmod tempor incididunt ut labor aliqua.</p></div>
  <div class="card" style="left:217px;top:78px"><span class="tag">02</span><h4>Services - 02</h4><p>Lorem ipsum dolor sit amet, consectetur adipisicing elit, sed do eiusmod tempor incididunt ut labor aliqua.</p></div>
  <div class="card" style="left:349px;top:80px"><span class="tag">03</span><h4>Services - 03</h4><p>Lorem ipsum dolor sit amet, consectetur adipisicing elit, sed do eiusmod tempor incididunt ut labor aliqua.</p></div>
  <div class="card" style="left:85px;top:178px"><span class="tag">04</span><h4>Services - 04</h4><p>Lorem ipsum dolor sit amet, consectetur adipisicing elit, sed do eiusmod tempor incididunt ut labor aliqua.</p></div>
  <div class="card" style="left:217px;top:181px"><span class="tag">05</span><h4>Services - 05</h4><p>Lorem ipsum dolor sit amet, consectetur adipisicing elit, sed do eiusmod tempor incididunt ut labor aliqua.</p></div>
  <div class="card" style="left:349px;top:184px"><span class="tag">06</span><h4>Services - 06</h4><p>Lorem ipsum dolor sit amet, consectetur adipisicing elit, sed do eiusmod tempor incididunt ut labor aliqua.</p></div>
  <footer class="footer">Copyright text here</footer>
  <span class="page-no">01</span>
</section>

<!-- Annual reports -->
<section class="slide s-reports">
  <header class="header"><h2>OUR ANNUAL REPORTS</h2><div class="brand"><span class="brand-dot"></span><span class="brand-name">Marisol Keene Coaching</span></div></header>
  <svg class="abs" style="left:0;top:0" width="558" height="313">
    <defs><linearGradient id="yogaTone" x1="0" y1="0" x2="1" y2="1"><stop offset="0" stop-color="#d9d4cc"/><stop offset=".6" stop-color="#b8c4c9"/><stop offset="1" stop-color="#6c93b0"/></linearGradient></defs>
    <path role="img" aria-label="Photo of women meditating in a yoga class" d="M0 42 H212 C 262 100, 250 230, 350 300 H0 Z" fill="url(#yogaTone)"/>
    <path d="M212 42 C 262 100, 250 230, 350 300" fill="none" stroke="#f7941d" stroke-width="5"/>
    <g fill="none" stroke-width="3.5" stroke="#f7941d">
      <circle cx="346" cy="94" r="24" stroke="#eee"/><circle cx="346" cy="94" r="24" stroke-dasharray="113 151" transform="rotate(-90 346 94)"/>
      <circle cx="346" cy="164" r="24" stroke="#eee"/><circle cx="346" cy="164" r="24" stroke-dasharray="75 151" transform="rotate(-90 346 164)"/>
      <circle cx="346" cy="234" r="24" stroke="#eee"/><circle cx="346" cy="234" r="24" stroke-dasharray="98 151" transform="rotate(-90 346 234)"/>
    </g>
    <g font-family="Poppins, sans-serif" font-weight="600" font-size="10" fill="#222" text-anchor="middle">
      <text x="346" y="98">75%</text><text x="346" y="168">50%</text><text x="346" y="238">65%</text>
    </g>
  </svg>
  <div class="stat" style="top:78px"><h4>Positive Feedback</h4><p class="lorem">Lorem ipsum dolor sit amet, consect eturadi piscing elit, sed do eiusmod tempor incid idunt utlabore</p></div>
  <div class="stat" style="top:148px"><h4>Returning Clients</h4><p class="lorem">Lorem ipsum dolor sit amet, consect eturadi piscing elit, sed do eiusmod tempor incid idunt utlabore</p></div>
  <div class="stat" style="top:218px"><h4>New Projects</h4><p class="lorem">Lorem ipsum dolor sit amet, consect eturadi piscing elit, sed do eiusmod tempor incid idunt utlabore</p></div>
  <footer class="footer">Copyright text here</footer>
  <span class="page-no">01</span>
</section>

</body>
</html>
```